Zielgruppe
Wir installieren Kälteanlagen für die Industrie, das Gewerbe und Privat. Kälteanlagen mit natürlichem Kältemittel CO2 und Klimaanlagen.
Aufgabenstellung
In unserem Eingangsbereich befindet sich ein Raumtrenner (siehe beigefügte Bilder). Darauf steht ein restaurierter historischer Kältekompressor. Ein altes Prospekt dieser Maschine finden Sie im Anhang. Wir würden gerne hinten auf dem Ständer eine beklebte Glasscheibe anbringen um unsere Besucher zu begrüßen und ggf. ein paar Infos zu dem Kältekompressor zu geben. Dafür soll ein Design erstellt werden. Die Fläche hinter dem Kompressor ist ca. 1,60 x 1,60 m groß. Der Kältekompressor an seinem höchsten Punkt ca. 1,10 m. Die Glasscheibe würden wir ca. 1,40 m x 0,8 m hoch machen, die wäre also teilweise verdeckt von dem Kompressor.

```html
<!DOCTYPE html>
<html lang="de">
<head>
<meta charset="utf-8">
<title>Willkommen – Glasscheibe Eingangsbereich</title>
<link rel="stylesheet" href="https://fonts.googleapis.com/css2?family=Saira+Condensed:wght@600;700;800&family=Open+Sans:wght@700&display=swap">
<style>
  :root {
    --page: #e9ecef;
    --ice-light: #d8eef8;
    --ice-mid: #7cc3e6;
    --ice-deep: #3f9fd2;
    --frost: #f4fbff;
    --band-blue: #2a7fc1;
    --brand-blue: #1f6fb3;
    --ink: #1d2a35;
    --white: #ffffff;
    --photo-grey: #8f969b;
    --photo-light: #d9dcde;
  }
  * { margin: 0; padding: 0; box-sizing: border-box; }
  html, body {
    width: 1200px; height: 831px; overflow: hidden;
    background: var(--page);
  }
  .glass-panel {
    position: absolute; left: 0; top: 72px;
    width: 1200px; height: 686px; overflow: hidden;
  }
  .frost-backdrop {
    position: absolute; inset: 0;
    background:
      radial-gradient(ellipse 62% 58% at 55% 50%, var(--ice-mid) 0%, var(--ice-deep) 55%, transparent 80%),
      radial-gradient(ellipse 100% 100% at 50% 50%, var(--ice-mid) 40%, var(--frost) 100%);
  }
  .headline {
    position: absolute; right: 85px; top: 98px;
    font-family: "Saira Condensed", sans-serif; font-weight: 700;
    font-size: 96px; line-height: 92px; text-align: right;
    color: var(--white); letter-spacing: 2px;
    text-shadow: 3px 3px 0 var(--ink);
  }
  .archive-photo {
    position: absolute; border: 5px solid var(--white);
    background: linear-gradient(135deg, var(--photo-light), var(--photo-grey));
    box-shadow: 2px 3px 6px rgba(0,0,0,.35);
  }
  .archive-photo.back { left: 240px; top: 200px; width: 160px; height: 170px; transform: rotate(-8deg); }
  .archive-photo.front { left: 115px; top: 250px; width: 180px; height: 130px; transform: rotate(10deg); }
  .machine-brand {
    position: absolute; left: 420px; top: 300px; width: 270px;
    font-family: "Saira Condensed", sans-serif; text-align: center; color: var(--ink);
  }
  .machine-brand .maker { font-weight: 700; font-size: 54px; line-height: 64px; color: var(--white); }
  .machine-brand .type { font-weight: 800; font-size: 30px; line-height: 34px; letter-spacing: 1px; }
  .machine-brand .model {
    font-weight: 800; font-size: 90px; line-height: 92px; color: var(--white);
    text-shadow: 3px 3px 0 var(--ink); margin-left: 90px;
  }
  .machine-brand .years {
    font-weight: 600; font-size: 30px; line-height: 34px; color: var(--white);
    text-shadow: 2px 2px 0 var(--ink); margin-left: 90px;
  }
  .company-band {
    position: absolute; left: 533px; top: 608px; width: 661px; height: 26px;
    background: var(--band-blue);
  }
  .company-band .trade {
    position: absolute; left: 150px; top: 1px;
    font-family: "Open Sans", sans-serif; font-weight: 700; font-size: 18px;
    color: var(--white); letter-spacing: 1px; line-height: 24px;
  }
  .company-name {
    position: absolute; left: 730px; top: 548px;
    font-family: "Saira Condensed", sans-serif; font-weight: 800;
    font-size: 60px; line-height: 60px; color: var(--ink); letter-spacing: 1px;
  }
  .company-square {
    position: absolute; left: 962px; top: 546px; width: 100px; height: 100px;
    background: var(--brand-blue); border: 4px solid var(--ink);
  }
</style>
</head>
<body>
  <section class="glass-panel">
    <div class="frost-backdrop" role="img" aria-label="Eisblaue Fläche mit Raureif-Kristallen am Rand"></div>

    <div class="archive-photo back" role="img" aria-label="Historisches Schwarzweißfoto einer Kälteanlage"></div>
    <div class="archive-photo front" role="img" aria-label="Historisches Schwarzweißfoto eines Maschinenraums"></div>

    <h1 class="headline">HERZLICH<br>WILLKOMMEN</h1>

    <div class="machine-brand">
      <div class="maker">Nordhag</div>
      <div class="type">KÄLTEAUTOMAT</div>
      <div class="model">„KV“</div>
      <div class="years">1939 - 55</div>
    </div>

    <div class="company-name">KALTHOF</div>
    <div class="company-band"><span class="trade">ELEKTRO-KÄLTEBAU</span></div>
    <div class="company-square"></div>
  </section>
</body>
</html>
```